continuing medical education travel company. luxury, professional, quality service

PLEASE USE THE REVISED LOGO FOR ALL CARD DESIGNS, NO SNAKE HEAD

Target Market(s)

physicians

Industry/Entity Type

Travel Industry

Contact Information for Business Card

luxury quality, spot uv, foil, rounded corners

Colors
0255a3
3176b5
cfdeed
aaaaaa
5c5c5c

Requirements
Must have
• navy, platinum, possible holographic

```html
<!DOCTYPE html>
<html lang="en">
<head>
<meta charset="utf-8">
<title>Veridel Travel – Business Card</title>
<link href="https://fonts.googleapis.com/css2?family=Arimo:wght@400;700&family=Roboto+Condensed:wght@400&display=swap" rel="stylesheet">
<style>
  :root {
    --navy: #0255a3;
    --navy-deep: #0a3f7d;
    --sky: #3176b5;
    --ice: #cfdeed;
    --platinum: #aaaaaa;
    --paper: #ffffff;
    --stage: #e6e8eb;
  }
  html, body {
    margin: 0;
    padding: 0;
    width: 1200px;
    height: 1200px;
    overflow: hidden;
    background: var(--stage);
  }
  .canvas {
    position: relative;
    width: 1200px;
    height: 1200px;
  }
  .card {
    position: absolute;
    left: 165px;
    width: 870px;
    height: 490px;
    border-radius: 10px;
    overflow: hidden;
    box-shadow: 0 4px 14px rgba(0,0,0,0.18);
  }
  .card--back {
    top: 80px;
    background: var(--navy);
  }
  .card--front {
    top: 630px;
    background: var(--navy);
    display: flex;
  }
  .brand {
    position: absolute;
    display: flex;
    align-items: center;
    gap: 18px;
    color: var(--paper);
    font-family: "Arimo", Arial, sans-serif;
    font-weight: 700;
    white-space: nowrap;
  }
  .brand__dot {
    border-radius: 50%;
    background: var(--ice);
    flex: none;
  }
  .card--back .brand {
    left: 50%;
    top: 50%;
    transform: translate(-50%, -50%);
    font-size: 54px;
    letter-spacing: 1px;
  }
  .card--back .brand__dot { width: 60px; height: 60px; }
  .front__info {
    position: relative;
    width: 540px;
    height: 100%;
    background: var(--paper);
    font-family: "Arimo", Arial, sans-serif;
    color: var(--navy);
  }
  .front__logo-panel {
    position: relative;
    flex: 1;
    background: var(--navy);
  }
  .front__logo-panel .brand {
    left: 50%;
    top: 50%;
    transform: translate(-50%, -50%);
    font-size: 30px;
    gap: 12px;
  }
  .front__logo-panel .brand__dot { width: 34px; height: 34px; }
  .person__name {
    position: absolute;
    top: 18px;
    left: 0;
    width: 100%;
    text-align: center;
    margin: 0;
    font-size: 50px;
    font-weight: 700;
    letter-spacing: 0.5px;
  }
  .person__title {
    position: absolute;
    top: 76px;
    left: 0;
    width: 100%;
    text-align: center;
    margin: 0;
    font-size: 30px;
    font-weight: 400;
  }
  .contact {
    position: absolute;
    top: 132px;
    left: 62px;
    margin: 0;
    padding: 0;
    list-style: none;
  }
  .contact__item {
    display: flex;
    align-items: center;
    gap: 8px;
    height: 31px;
    font-size: 22px;
  }
  .contact__icon { width: 24px; height: 24px; flex: none; }
  .address {
    position: absolute;
    left: 29px;
    bottom: 20px;
    margin: 0;
    font-family: "Roboto Condensed", "Arial Narrow", sans-serif;
    font-size: 27px;
  }
</style>
</head>
<body>
<main class="canvas">

  <section class="card card--back" aria-label="Card back">
    <div class="brand">
      <span class="brand__dot"></span>
      <span class="brand__name">VERIDEL TRAVEL</span>
    </div>
  </section>

  <section class="card card--front" aria-label="Card front">
    <div class="front__info">
      <h1 class="person__name">LAURA BENNETT</h1>
      <p class="person__title">Principal</p>
      <ul class="contact">
        <li class="contact__item">
          <svg class="contact__icon" viewBox="0 0 24 24" aria-hidden="true">
            <circle cx="12" cy="12" r="12" fill="var(--navy)"/>
            <path d="M8.2 6.5c.5-.4 1.1-.3 1.4.2l1.1 1.8c.3.5.2 1-.2 1.3l-.8.6c.6 1.4 1.6 2.5 3 3.1l.6-.8c.3-.4.9-.5 1.3-.2l1.8 1.1c.5.3.6 1 .2 1.4l-.9 1c-.6.6-1.5.8-2.3.5-3-1.2-5.3-3.5-6.5-6.5-.3-.8-.1-1.7.5-2.3z" fill="#fff"/>
          </svg>
          555.210.4870
        </li>
        <li class="contact__item">
          <svg class="contact__icon" viewBox="0 0 24 24" aria-hidden="true">
            <circle cx="12" cy="12" r="12" fill="var(--navy)"/>
            <rect x="6" y="8" width="12" height="8.5" rx="1" fill="#fff"/>
            <path d="M6.5 8.5 12 13l5.5-4.5M6.5 16l4-3.5M17.5 16l-4-3.5" stroke="var(--navy)" stroke-width="1" fill="none"/>
          </svg>
          lbennett@veridel.com
        </li>
        <li class="contact__item">
          <svg class="contact__icon" viewBox="0 0 24 24" aria-hidden="true">
            <circle cx="12" cy="12" r="12" fill="var(--navy)"/>
            <g stroke="#fff" stroke-width="1.2" fill="none">
              <circle cx="12" cy="12" r="6.5"/>
              <ellipse cx="12" cy="12" rx="2.8" ry="6.5"/>
              <path d="M5.5 12h13M6.5 9h11M6.5 15h11"/>
            </g>
          </svg>
          veridel.com
        </li>
      </ul>
      <p class="address">48 Harbour Lane, Lakeview,QC H0H 0H0</p>
    </div>
    <div class="front__logo-panel">
      <div class="brand">
        <span class="brand__dot"></span>
        <span class="brand__name">VERIDEL TRAVEL</span>
      </div>
    </div>
  </section>

</main>
</body>
</html>
```